Creative Stationary for Solo Law Firm

I am looking for stationary designs for my solo law firm called TM Halvorsen Law PLLC. My logo is attached. I'd like the logo incorporated into the design.

I'm looking for a stationary design that is a bit outside of the box and not too standard or boring. The final design should communicate professionalism.

Target Market(s)

United States Clients, Opposing Counsel

Industry/Entity Type

Legal

Font styles to use
Sans Serif

Requirements
Must have
• The stationary design must incorporate my logo design attached. The design itself must be creative. The envelope design must follow standard United States designs with room for the postage stamp at the top right corner and space for the recipient's address in the middle.

```html
<!DOCTYPE html>
<html lang="en">
<head>
<meta charset="utf-8">
<title>TM Halvorsen Law — Business Card</title>
<link href="https://fonts.googleapis.com/css2?family=Cinzel:wght@400;500&family=Open+Sans:wght@400&display=swap" rel="stylesheet">
<style>
  :root {
    --bg: #e8e7e3;
    --card: #ffffff;
    --navy: #1f2f6e;
    --ink: #4a4a4a;
    --muted: #7a7a7a;
    --rule: #b9b9b9;
    --panel-light: #e4e4e4;
    --panel-dark: #cfcfcf;
  }
  * { margin: 0; padding: 0; box-sizing: border-box; }
  html, body { width: 1200px; height: 950px; overflow: hidden; background: var(--bg); }
  .canvas {
    width: 1200px; height: 950px;
    display: flex; flex-direction: column; align-items: center; justify-content: center;
    gap: 50px;
  }
  .card {
    width: 700px; height: 400px;
    background: var(--card);
    position: relative;
    overflow: hidden;
    box-shadow: 0 2px 10px rgba(0,0,0,0.12);
  }
  /* Front */
  .card-front .monogram-panel {
    position: absolute; left: 0; top: 0; bottom: 0; width: 240px;
    background: linear-gradient(160deg, var(--panel-light), var(--panel-dark));
  }
  .card-front .edge-stripe {
    position: absolute; right: 0; top: 0; bottom: 0; width: 14px;
    background: var(--navy);
  }
  .card-front .details {
    position: absolute; left: 285px; top: 44px; right: 60px;
  }
  .firm-name {
    font-family: "Cinzel", serif;
    color: var(--navy);
    font-weight: 500;
    font-size: 32px;
    letter-spacing: 0.5px;
    line-height: 1.1;
  }
  .divider {
    border: 0; border-top: 1px dashed var(--rule);
    margin: 16px 0;
  }
  .person-name {
    font-family: "Cinzel", serif; color: var(--navy);
    font-size: 23px; line-height: 1.15;
  }
  .person-title {
    font-family: "Cinzel", serif; color: var(--muted);
    font-size: 15px; margin-top: 4px;
  }
  .address, .contact-list {
    font-family: "Open Sans", sans-serif; color: var(--ink);
    font-size: 15px; line-height: 1.55;
  }
  .contact-list { list-style: none; }
  .contact-list li { display: flex; align-items: center; gap: 10px; }
  .contact-list svg { width: 15px; height: 15px; fill: var(--navy); flex: none; }
  /* Back */
  .card-back { display: flex; align-items: center; justify-content: center; }
  .card-back .firm-name { font-size: 44px; }
</style>
</head>
<body>
<main class="canvas">
  <section class="card card-front">
    <div class="monogram-panel" role="img" aria-label="Grey panel where the firm monogram decoration sits"></div>
    <div class="edge-stripe"></div>
    <div class="details">
      <h1 class="firm-name">TM Halvorsen Law</h1>
      <hr class="divider">
      <p class="person-name">Erik Lindqvist</p>
      <p class="person-title">CEO/Founder</p>
      <hr class="divider">
      <p class="address">412 Birchwood Court<br>Juneau, Alaska 99801</p>
      <hr class="divider">
      <ul class="contact-list">
        <li><svg viewBox="0 0 16 16"><path d="M3.5 1.5l2.5 0 1 3.5-1.7 1.2a8 8 0 0 0 4.5 4.5L11 9l3.5 1 0 2.5c0 1-1 2-2 2A11 11 0 0 1 1.5 3.5c0-1 1-2 2-2z"/></svg>907 555 0182</li>
        <li><svg viewBox="0 0 16 16"><path d="M2 2h12v12H2z M4 4v8h8V4z"/></svg>907 555 0147</li>
        <li><svg viewBox="0 0 16 16"><path d="M1 3h14v10H1z M2.5 4.5v.3L8 9l5.5-4.2v-.3z"/></svg>erik@halvorsenlaw.com</li>
        <li><svg viewBox="0 0 16 16"><circle cx="8" cy="8" r="7"/></svg>www.halvorsenlaw.com</li>
      </ul>
    </div>
  </section>

  <section class="card card-back">
    <h2 class="firm-name">TM Halvorsen Law</h2>
  </section>
</main>
</body>
</html>
```